New bussiness card, using company logo.
Lachlan Voss
Manager/Director
Birch Property Developments
Po Box 4657
Wattlebrook Central
Kra
0455 386 218
lachlan@birchpropertydevelopments
eye catching, vibrant colours, professional

```html
<!DOCTYPE html>
<html lang="en">
<head>
<meta charset="utf-8">
<title>Birch Property Developments – Business Card</title>
<link rel="stylesheet" href="https://fonts.googleapis.com/css2?family=Montserrat:wght@700&family=Questrial&display=swap">
<style>
  :root {
    --page: #ffffff;
    --card-dark: #231f20;
    --card-band: #f28a33;
    --card-edge: #d9d9d9;
    --text-light: #ffffff;
    --brand-text: #e6e6e6;
    --brand-accent: #6cc04a;
  }
  html, body {
    margin: 0;
    padding: 0;
    width: 1200px;
    height: 900px;
    overflow: hidden;
    background: var(--page);
  }
  .canvas {
    position: relative;
    width: 1200px;
    height: 900px;
  }
  .card {
    position: absolute;
    left: 98px;
    top: 143px;
    width: 1004px;
    height: 614px;
    outline: 1px solid var(--card-edge);
    overflow: hidden;
    font-family: "Questrial", sans-serif;
    color: var(--text-light);
  }
  .card-top {
    position: absolute;
    left: 0; top: 0;
    width: 100%;
    height: 422px;
    background: var(--card-dark);
  }
  .brand {
    position: absolute;
    left: 38px;
    top: 236px;
    display: flex;
    align-items: center;
    gap: 18px;
  }
  .brand-mark {
    width: 34px;
    height: 34px;
    background: var(--brand-accent);
    flex: none;
  }
  .brand-name {
    margin: 0;
    font-family: "Questrial", sans-serif;
    font-weight: 400;
    font-size: 40px;
    line-height: 46px;
    color: var(--brand-text);
  }
  .card-band {
    position: absolute;
    left: 0;
    top: 422px;
    width: 100%;
    height: 192px;
    background: var(--card-band);
  }
  .person {
    position: absolute;
    left: 18px;
    top: 14px;
    width: 318px;
    text-align: center;
  }
  .person-name {
    margin: 0;
    font-family: "Montserrat", sans-serif;
    font-weight: 700;
    font-size: 30px;
    letter-spacing: 1px;
    line-height: 40px;
  }
  .person-role {
    margin: 0;
    font-size: 32px;
    letter-spacing: 1.5px;
    line-height: 40px;
  }
  .contact {
    position: absolute;
    right: 27px;
    top: 14px;
    text-align: right;
    font-style: normal;
    white-space: nowrap;
  }
  .contact-company {
    margin: 0;
    font-size: 34px;
    letter-spacing: 1.5px;
    line-height: 40px;
  }
  .contact-line {
    margin: 0;
    font-size: 26px;
    letter-spacing: 1px;
    line-height: 30px;
  }
</style>
</head>
<body>
<div class="canvas">
  <section class="card">
    <div class="card-top">
      <div class="brand">
        <span class="brand-mark"></span>
        <p class="brand-name">Birch Property<br>Developments</p>
      </div>
    </div>
    <div class="card-band">
      <div class="person">
        <p class="person-name">Lachlan Voss</p>
        <p class="person-role">Manager/Director</p>
      </div>
      <address class="contact">
        <p class="contact-company">Birch Property Developments</p>
        <p class="contact-line">Po Box 4657, Wattlebrook Central</p>
        <p class="contact-line">Kra</p>
        <p class="contact-line">0455 386 218</p>
        <p class="contact-line">lachlan@birchpropertydevelopments</p>
      </address>
    </div>
  </section>
</div>
</body>
</html>
```